Bref créative
Business card and stationary for Maplecrest Vision Studio Eye Clinic
Maplecrest Vision Studio / (Clear Sight Daily)
Professional
Dr. Marcus Pell, O.D.
Optometric Physician
Bayline Office
2864 Larkwood Ave
Harborton, FL. 34990
Emergency:813-555-0487
maplecrestvisionstudiohub@mailbox-demo.net
www.maplecrestvisionstudio-demo.com
Appointment
Date:_______ @ ______ AM / PM
WWW.MAPLECRESTVISIONSTUDIO-DEMO.COM
if unable to keep appointment kindly give 24 hours notice.
I need a business card and brochure made for my office with the new logo.

```html
<!DOCTYPE html>
<html lang="en">
<head>
<meta charset="utf-8">
<title>Maplecrest Vision Studio – Business Card</title>
<link href="https://fonts.googleapis.com/css2?family=Open+Sans:ital,wght@0,400;0,600;0,700;1,400&display=swap" rel="stylesheet">
<style>
  :root {
    --backdrop: #e9e6e2;
    --card: #ffffff;
    --band: #3a8cc0;
    --band-dark: #2f7aab;
    --ink: #1f3550;
    --accent: #3a8cc0;
    --rule: #c9ced3;
    --white: #ffffff;
  }
  * { box-sizing: border-box; margin: 0; padding: 0; }
  html, body { width: 1200px; height: 902px; overflow: hidden; }
  body {
    background: var(--backdrop);
    font-family: "Open Sans", Arial, sans-serif;
    position: relative;
  }
  .business-card {
    position: absolute;
    left: 100px; top: 165px;
    width: 1000px; height: 572px;
    background: var(--card);
    box-shadow: 0 10px 30px rgba(0,0,0,0.18);
    overflow: hidden;
  }
  .brand {
    position: absolute;
    left: 70px; top: 70px;
  }
  .brand-row { display: flex; align-items: center; gap: 16px; }
  .brand-mark {
    width: 34px; height: 34px; border-radius: 50%;
    background: var(--accent);
  }
  .brand-name {
    font-size: 40px; font-weight: 600; color: var(--ink);
    letter-spacing: 0.5px; line-height: 1.1;
  }
  .brand-tagline {
    margin-top: 10px; margin-left: 50px;
    font-size: 20px; font-style: italic; color: var(--accent);
  }
  .band-rule {
    position: absolute; left: 0; right: 0; top: 268px;
    height: 4px; background: var(--rule);
  }
  .contact-band {
    position: absolute; left: 0; right: 0; top: 276px;
    height: 196px; background: var(--band);
    border-bottom: 4px solid var(--band-dark);
    color: var(--white);
  }
  .contact-list {
    list-style: none;
    position: absolute; left: 40px; top: 26px;
    font-size: 15px; line-height: 22px;
  }
  .contact-list li { display: flex; align-items: flex-start; gap: 10px; }
  .contact-icon {
    flex: none; width: 16px; height: 16px; margin-top: 3px;
    border-radius: 50%; background: var(--white);
    display: flex; align-items: center; justify-content: center;
  }
  .contact-icon svg { width: 10px; height: 10px; fill: var(--band); }
  .doctor {
    position: absolute; right: 50px; top: 44px; text-align: right;
  }
  .doctor-name { font-size: 22px; font-weight: 700; }
  .doctor-title { font-size: 18px; margin-top: 4px; }
</style>
</head>
<body>
  <div class="business-card">
    <div class="brand">
      <div class="brand-row">
        <span class="brand-mark"></span>
        <span class="brand-name">Maplecrest Vision Studio</span>
      </div>
      <p class="brand-tagline">Clear Sight Daily</p>
    </div>

    <div class="band-rule"></div>

    <section class="contact-band">
      <ul class="contact-list">
        <li>
          <span class="contact-icon"><svg viewBox="0 0 10 10"><path d="M5 0.5a3 3 0 0 0-3 3c0 2.3 3 6 3 6s3-3.7 3-6a3 3 0 0 0-3-3zm0 4.2a1.2 1.2 0 1 1 0-2.4 1.2 1.2 0 0 1 0 2.4z"/></svg></span>
          <span>Bayline Office 2864 Larkwood Ave<br>Harborton, FL. 34990</span>
        </li>
        <li>
          <span class="contact-icon"><svg viewBox="0 0 10 10"><path d="M2.2 1l1.5 1.8-.8 1.1c.6 1.2 1.4 2 2.6 2.6l1.1-.8L8.4 7.2 7.6 9C4.2 8.6 1.4 5.8 1 2.4z"/></svg></span>
          <span>813-555-0192</span>
        </li>
        <li>
          <span class="contact-icon"><svg viewBox="0 0 10 10"><path d="M2.2 1l1.5 1.8-.8 1.1c.6 1.2 1.4 2 2.6 2.6l1.1-.8L8.4 7.2 7.6 9C4.2 8.6 1.4 5.8 1 2.4z"/></svg></span>
          <span>813-555-0487</span>
        </li>
        <li>
          <span class="contact-icon"><svg viewBox="0 0 10 10"><path d="M1 2.5h8v5H1z"/></svg></span>
          <span>813-555-0261</span>
        </li>
        <li>
          <span class="contact-icon"><svg viewBox="0 0 10 10"><path d="M1 2.5h8v5H1zM1 2.5l4 3 4-3" stroke="#fff" stroke-width="0.6"/></svg></span>
          <span>maplecrestvisionstudiohub@mailbox-demo.net</span>
        </li>
        <li>
          <span class="contact-icon"><svg viewBox="0 0 10 10"><circle cx="5" cy="5" r="3.6"/></svg></span>
          <span>www.maplecrestvisionstudio-demo.com</span>
        </li>
      </ul>

      <div class="doctor">
        <p class="doctor-name">Dr. Marcus Pell, O.D.</p>
        <p class="doctor-title">Optometric Physician</p>
      </div>
    </section>
  </div>
</body>
</html>
```